Selam-Kaveh - Promote and Support a community

Design a website for Ethiopean Community. the design should be friendly, easy to navigate and maintain the look & feel of the Ethiopian culture. a proposed logo is attached but it can be change according to your recommendations. This is a project we are doing at a discount rate as it supports a weak community.
Please visit their current website http://www.selam-kaveh.example.org/index.php?lang=en

Target Market(s)

Community members, potential doners

Industry/Entity Type

community

Number of Pages Required

1 page

Font styles to use
Sans Serif

Requirements
Must have
• easy to navigate friendly interface

```html
<!DOCTYPE html>
<html lang="en">
<head>
<meta charset="utf-8">
<title>Selam Kaveh</title>
<link href="https://fonts.googleapis.com/css2?family=Poppins:wght@300;400;500;600;700&display=swap" rel="stylesheet">
<style>
:root{
  --green:#12a112;
  --green-dark:#0b8a0b;
  --yellow:#f6c225;
  --red:#d23b36;
  --cream:#fdf2e4;
  --peach:#fce9d6;
  --ink:#1b1b1b;
  --muted:#555;
  --dark:#2e2e2e;
  --white:#fff;
  --soft:#d6d6d6;
}
*{box-sizing:border-box;margin:0;padding:0}
html,body{width:1200px;height:4027px;overflow:hidden}
body{font-family:'Poppins',sans-serif;color:var(--ink);background:var(--white);position:relative}
.abs{position:absolute}
.photo{display:block}

/* header */
.header{position:absolute;left:0;top:0;width:1200px;height:102px;background:var(--cream);z-index:5}
.brand{position:absolute;left:20px;top:20px;width:166px;height:166px;border-radius:50%;background:var(--white);border:6px solid var(--red);display:flex;align-items:center;justify-content:center;z-index:6;font-weight:700;font-size:22px;color:var(--red);text-align:center;line-height:1.1}
.topline{position:absolute;right:40px;top:10px;display:flex;align-items:center;gap:22px;font-size:12px}
.topline .lbl{font-size:10px;color:var(--muted)}
.topline .item{display:flex;align-items:center;gap:8px;font-weight:500}
.ico{width:22px;height:22px;border-radius:50%;background:var(--yellow);display:inline-flex;align-items:center;justify-content:center}
.lang{border:2px solid var(--yellow);border-radius:20px;padding:4px 16px;font-size:17px;display:flex;gap:8px;align-items:center}
.nav{position:absolute;left:298px;top:64px;display:flex;align-items:center;font-size:11px;font-weight:500}
.nav a{color:var(--ink);text-decoration:none}
.nav .caret{font-size:8px;margin-left:6px}
.nav .active{position:relative}
.nav .active:after{content:"";position:absolute;left:0;right:0;bottom:-18px;height:4px;background:var(--green)}
.btn{display:inline-block;border-radius:20px;color:var(--white);font-weight:600;font-size:11px;text-align:center;text-decoration:none}
.btn-red{background:var(--red)}
.btn-green{background:var(--green)}
.btn-yellow{background:var(--yellow);color:var(--white)}

/* hero */
.hero-photo{position:absolute;left:0;top:102px;width:1200px;height:492px;background:linear-gradient(120deg,#b42d6b 0%,#e0558e 25%,#7a3a9a 45%,#d97a3a 65%,#c93a70 85%,#6a2f7a 100%)}
.hero-shade{position:absolute;left:0;top:102px;width:1200px;height:492px;background:rgba(60,10,40,.35)}
.hero-title{position:absolute;left:0;width:1200px;text-align:center;color:var(--white)}
.hl{display:inline-block;background:linear-gradient(transparent 70%,var(--yellow) 70%,var(--yellow) 88%,transparent 88%)}

.cards{position:absolute;left:150px;top:503px;width:900px;height:250px;display:flex}
.card{width:300px;height:250px;position:relative;color:var(--white);text-align:center}
.card-about{background:var(--green)}
.card-prog{background:var(--yellow)}
.card-support{background:var(--red)}
.dash{width:40px;height:2px;background:var(--white);margin:0 auto}

/* welcome */
.kicker{font-size:22px;font-weight:300;color:#777}
.h2{font-size:53px;font-weight:700;line-height:1}
.body{font-size:11px;line-height:18px;color:#333}
.note{position:absolute;left:117px;top:1287px;width:438px;height:182px;background:var(--peach);padding:28px 32px}

/* banner */
.banner{position:absolute;left:0;top:1563px;width:1200px;height:278px;background:linear-gradient(110deg,#5a2a14,#a5561f 40%,#7a3a18 70%,#4a2210)}
.green-sec{position:absolute;left:0;top:1841px;width:1200px;height:722px;background:var(--green)}
.pcard{position:absolute;top:2072px;width:209px;height:341px;background:var(--white)}
.pcard .pimg{height:167px}
.pcard h4{font-size:13px;font-weight:600;line-height:16px;margin:28px 25px 6px}
.pcard p{font-size:10.5px;line-height:18px;color:#555;margin:0 25px}
.pcard .more{font-size:10px;font-weight:600;color:var(--red);margin:12px 25px 0}

/* contact */
.field{position:absolute;background:#f1f1f1;border:1px solid #e4e4e4;font-size:9px;color:#555;padding:12px 18px}

.yellow-sec{position:absolute;left:0;top:3023px;width:1200px;height:290px;background:linear-gradient(120deg,#e5a617,#f6c225 50%,#d99812)}
.partners{position:absolute;left:0;top:3313px;width:1200px;height:143px;background:var(--cream)}
.badge{position:absolute;top:3356px;width:62px;height:58px;border-radius:8px;background:#c9c4bd}

.footer{position:absolute;left:0;top:3606px;width:1200px;height:421px;background:var(--dark)}
.fcol{position:absolute;top:3766px;width:200px;text-align:center;color:var(--white)}
.fcol .lbl{font-size:10px;color:var(--soft);margin-top:10px}
.fcol .val{font-size:11px;margin-top:6px;color:var(--white)}
.fcol .bar{height:4px;background:var(--red);margin-top:24px}
.fnav{position:absolute;left:0;top:3934px;width:1200px;font-size:10px;font-weight:500;color:var(--white)}
.fnav span{position:absolute}
.copy{color:var(--soft)}
</style>
</head>
<body>

<header class="header">
  <div class="topline">
    <span class="lbl">Call us at:</span>
    <span class="item"><span class="ico"><svg width="12" height="12" viewBox="0 0 24 24"><path fill="#fff" d="M6.6 10.8a15 15 0 0 0 6.6 6.6l2.2-2.2a1 1 0 0 1 1-.25 11 11 0 0 0 3.6.6 1 1 0 0 1 1 1V20a1 1 0 0 1-1 1A17 17 0 0 1 3 4a1 1 0 0 1 1-1h3.5a1 1 0 0 1 1 1 11 11 0 0 0 .6 3.6 1 1 0 0 1-.25 1z"/></svg></span>04-5550172</span>
    <span class="item" style="font-size:11px"><span class="ico"><svg width="12" height="12" viewBox="0 0 24 24"><path fill="#fff" d="M3 5h18v14H3zm2 2v.5l7 4.5 7-4.5V7z"/></svg></span>selamkaveh@example.org</span>
    <span class="lang"><span class="ico" style="width:18px;height:18px"></span>עברית</span>
  </div>
  <nav class="nav">
    <a class="active" style="margin-right:56px">HOME</a>
    <a style="margin-right:44px">ABOUT<span class="caret">▼</span></a>
    <a style="margin-right:56px">THE COMMUNITY</a>
    <a style="margin-right:44px">PROGRAMS<span class="caret">▼</span></a>
    <a style="margin-right:44px">NEWS<span class="caret">▼</span></a>
    <a style="margin-right:64px">ADVOCACY</a>
    <a style="margin-right:60px">PARTNERS</a>
    <a class="btn btn-red" style="padding:11px 20px;margin-top:-2px">SUPPORT US</a>
  </nav>
</header>
<div class="brand">Selam<br>Kaveh</div>

<div class="hero-photo photo" role="img" aria-label="Close-up of colourful hand-woven Ethiopian baskets"></div>
<div class="hero-shade"></div>
<svg class="abs" style="left:0;top:570px" width="1200" height="30" viewBox="0 0 1200 30" aria-hidden="true"><path fill="#fff" d="M0 22 L40 16 L90 20 L140 12 L200 18 L260 10 L330 17 L400 11 L470 19 L540 13 L610 18 L690 10 L760 16 L830 12 L900 19 L970 11 L1040 17 L1110 12 L1200 18 L1200 30 L0 30Z"/></svg>
<div class="hero-title" style="top:222px;font-size:62px;font-weight:700;line-height:1"><span class="hl">Selam Kaveh</span></div>
<div class="hero-title" style="top:295px;font-size:13px">("health" in both Amharic &amp; Hebrew)</div>
<div class="hero-title" style="top:314px;font-size:29px;font-weight:500;line-height:34px">is dedicated to improving the health of the<br>Ethiopian Israeli community.</div>

<div class="cards">
  <div class="card card-about">
    <div class="photo" role="img" aria-label="Group photo of the organisation's team" style="position:absolute;left:0;top:0;width:300px;height:190px;background:linear-gradient(180deg,#6f8a8a,#9fb0a6 60%,var(--green))"></div>
    <div style="position:absolute;left:24px;top:160px;text-align:left"><div style="font-size:29px;font-weight:600;line-height:1">About</div><div style="font-size:12px;font-weight:600">Selam Kaveh</div></div>
    <div style="position:absolute;left:130px;top:160px;text-align:left;font-size:12px;line-height:19px">› Board<br>› Team<br>› Missions and Goals</div>
  </div>
  <div class="card card-prog">
    <div class="dash" style="margin-top:78px"></div>
    <div style="font-size:29px;font-weight:500;margin-top:14px">Programs</div>
    <a class="btn btn-red" style="margin-top:14px;padding:10px 22px;font-size:10px">LEARN ABOUT OUR PROGRAMS</a>
  </div>
  <div class="card card-support">
    <div class="dash" style="margin-top:46px;background:var(--yellow)"></div>
    <div style="font-size:29px;font-weight:600;margin-top:6px">Support Us</div>
    <div style="font-size:10px;line-height:15px;margin:6px 50px 0">Selam Kaveh non-profit organization operates to promote the ethiopian israel community healthcare, using donations and government funding.</div>
    <a class="btn btn-green" style="margin-top:14px;padding:10px 18px;font-size:10px">DONATE NOW</a>
  </div>
</div>

<div class="abs kicker" style="left:150px;top:834px">Welcome to</div>
<div class="abs h2" style="left:150px;top:872px"><span class="hl">Selam Kaveh</span></div>
<div class="abs body" style="left:150px;top:938px;width:372px">
  <p>Aliyah (immigration) from Ethiopia to Israel and the transition to a sedentary lifestyle has resulted in the emergence of chronic diseases, in particular diabetes. While only 0.4% of the new immigrants were diagnosed with Type 2 diabetes upon arrival, by the time they had lived in Israel for ten years the figure had risen to 18% - three times as many as in the general population. The incidence of hypertension, obesity, asthma and Type 1 diabetes had also increased dramatically.</p>
  <p style="margin-top:18px"><b>Selam Kaveh was founded in 1999 by Dr. Miriam Adler, Head of the Endocrinology Unit at the Carmel Valley Medical Center.</b> Her experience with Ethiopian patients made her realize that medical treatment could not succeed without culturally competent communication. Selam Kaveh has developed into a small but dedicated NGO, delivering services throughout Israel with the backing and cooperation of a wide range of local and national bodies, including the Ministry of Health, the Ministry of Immigration, the absorption services, municipalities, the HMOs and hospitals.</p>
</div>
<div class="note body" style="padding:30px 34px">Today the Selam Kaveh team comprises eight Ethiopian-Israeli healthcare professionals, three Amharic-speaking medical interpreters and four health promotion specialists familiar with the Ethiopian immigrant community. Organizations within Israel and beyond now look to Selam Kaveh's programs for inspiration in their efforts to develop meaningful prevention strategies for improving the health of immigrants and minority communities.</div>

<svg class="abs" style="left:618px;top:826px" width="458" height="458" aria-hidden="true"><circle cx="229" cy="229" r="226" fill="none" stroke="#f7e6c4" stroke-width="2"/></svg>
<div class="abs photo" role="img" aria-label="Crowd of community members at a gathering" style="left:644px;top:852px;width:406px;height:406px;border-radius:50%;background:radial-gradient(circle at 40% 40%,#8a7a6a,#4a3a30 60%,#2a201a)"></div>
<div class="abs photo" role="img" aria-label="Team members holding a certificate" style="left:738px;top:1170px;width:212px;height:212px;border-radius:50%;border:5px solid var(--white);background:linear-gradient(160deg,#a9b5c0,#7e6e60 60%,#5a4a40)"></div>
<a class="abs btn btn-yellow" style="left:744px;top:1412px;width:208px;padding:11px 0;font-size:10px">LEARN MORE ABOUT SELAM KAVEH</a>

<div class="banner photo" role="img" aria-label="Warm-toned photo of a woven basket being held"></div>
<div class="abs" style="left:0;top:1563px;width:1200px;height:278px;background:rgba(70,30,10,.45)"></div>
<div class="abs" style="left:0;top:1624px;width:1200px;text-align:center;color:var(--white)">
  <div style="font-size:12px;font-weight:500;line-height:15px">Selam means health in Amharic, and also signifies a jewel basket: an<br>expensive and unique gift to preserve.</div>
  <div style="font-size:29px;font-weight:500;line-height:34px;margin-top:6px">Kaveh means health in Hebrew.</div>
  <div style="font-size:29px;font-weight:500;line-height:34px;color:var(--yellow)">Health is a gift to be preserved</div>
</div>

<div class="green-sec"></div>
<div class="abs photo" role="img" aria-label="Woven Ethiopian jewel basket" style="left:530px;top:1778px;width:140px;height:126px;border-radius:50% 50% 45% 45%;background:radial-gradient(circle at 50% 40%,#f2c233,#2e8a2e 55%,#b8302c)"></div>
<div class="abs" style="left:0;top:1950px;width:1200px;text-align:center;color:var(--white);font-size:22px;font-weight:300">Selam Kaveh</div>
<div class="abs h2" style="left:0;top:1976px;width:1200px;text-align:center;color:var(--white)"><span class="hl">Programs</span></div>

<div class="pcard" style="left:150px"><div class="pimg photo" role="img" aria-label="Women attending a health presentation" style="background:linear-gradient(160deg,#cfd6dc,#8a8f96)"></div><h4>Health &amp; Education<br>Presentations</h4><p>To spread awareness of a health promoting lifestyle and an understanding of diabetes.</p><div class="more">READ MORE »</div></div>
<div class="pcard" style="left:380px"><div class="pimg photo" role="img" aria-label="Visitors at a regional health fair" style="background:linear-gradient(160deg,#d7c9c0,#9a7f8a)"></div><h4>Regional<br>Health Fairs</h4><p>Every year, Selam Kaveh holds around 5 regional health fairs where members...</p><div class="more">READ MORE »</div></div>
<div class="pcard" style="left:610px"><div class="pimg photo" role="img" aria-label="Presenter in a radio studio" style="background:linear-gradient(160deg,#c8cdd6,#5d6270)"></div><h4>Amharic<br>Radio Program</h4><p>To reach the widest audience Selam Kaveh produces a fortnightly radio program...</p><div class="more">READ MORE »</div></div>
<div class="pcard" style="left:840px"><div class="pimg photo" role="img" aria-label="Support group activity with balloons" style="background:linear-gradient(160deg,#bcd0e0,#8aa0b6)"></div><h4>Therapeutic<br>Support Groups</h4><p>In partnership with Dr. Daniel Ross of Bridges of Care and Regional Health...</p><div class="more">READ MORE »</div></div>

<a class="abs btn btn-yellow" style="left:548px;top:2460px;width:103px;padding:10px 0;font-size:10px">VIEW MORE</a>
<svg class="abs" style="left:0;top:2550px" width="1200" height="20" viewBox="0 0 1200 20" aria-hidden="true"><path fill="#fff" d="M0 10 L30 6 L70 12 L120 5 L170 11 L230 6 L290 12 L350 5 L420 11 L480 6 L550 12 L620 5 L690 11 L760 6 L830 12 L900 5 L970 11 L1040 6 L1110 12 L1200 6 L1200 20 L0 20Z"/></svg>

<div class="abs kicker" style="left:0;top:2644px;width:1200px;text-align:center">Get Connected</div>
<div class="abs h2" style="left:0;top:2680px;width:1200px;text-align:center"><span class="hl">Contact Us</span></div>
<div class="field" style="left:240px;top:2753px;width:354px;height:35px">Name:</div>
<div class="field" style="left:240px;top:2803px;width:354px;height:35px">Phone:</div>
<div class="field" style="left:240px;top:2853px;width:354px;height:35px">Email:</div>
<div class="field" style="left:606px;top:2753px;width:352px;height:136px;padding-top:10px">Describe your request:</div>
<a class="abs btn btn-green" style="left:541px;top:2920px;width:101px;padding:10px 0;font-size:10px">SUBMIT</a>

<div class="yellow-sec photo" role="img" aria-label="Yellow-tinted photo of community members"></div>
<div class="abs" style="left:0;top:3095px;width:1200px;text-align:center;color:var(--white);font-size:53px;font-weight:600">What You Can Do</div>
<a class="abs btn btn-red" style="left:541px;top:3166px;width:118px;padding:10px 0">SUPPORT US</a>
<div class="abs" style="left:0;top:3216px;width:1200px;text-align:center;color:var(--white);font-size:9px">Non-Profit Registration Number: 580123456</div>

<div class="partners"></div>
<div class="badge" style="left:244px"></div>
<div class="badge" style="left:353px;width:96px;height:30px;top:3370px"></div>
<div class="badge" style="left:500px"></div>
<div class="badge" style="left:620px;width:88px;height:48px;top:3362px"></div>
<div class="badge" style="left:764px;width:44px;height:70px;top:3348px"></div>
<div class="badge" style="left:866px;width:92px;height:34px;top:3368px"></div>

<div class="abs" style="left:0;top:3498px;width:1200px;text-align:center;font-size:12px;font-weight:500;line-height:16px">Selam Kaveh believes that fostering an informed, active health leadership from within the<br>community itself is key to achieving its goals.</div>

<footer class="footer"></footer>
<div class="brand" style="left:517px;top:3558px">Selam<br>Kaveh</div>
<div class="fcol" style="left:261px">
  <svg width="22" height="22" viewBox="0 0 22 22"><circle cx="11" cy="11" r="10" fill="none" stroke="#f6c225" stroke-width="1.5"/><path d="M11 5a4 4 0 0 0-4 4c0 3 4 8 4 8s4-5 4-8a4 4 0 0 0-4-4z" fill="none" stroke="#fff" stroke-width="1.2"/></svg>
  <div class="lbl">office</div><div class="val">Harimon 12/4 POB 2210 Netanya, 42100</div><div class="bar"></div>
</div>
<div class="fcol" style="left:500px">
  <svg width="22" height="22" viewBox="0 0 22 22"><circle cx="11" cy="11" r="10" fill="none" stroke="#f6c225" stroke-width="1.5"/><path d="M7 7l2 0 1 3-1.5 1a7 7 0 0 0 3 3l1-1.5 3 1 0 2a1 1 0 0 1-1 1A9 9 0 0 1 6 8a1 1 0 0 1 1-1z" fill="#fff"/></svg>
  <div class="lbl">phone</div><div class="val" style="font-size:18px;font-weight:500;margin-top:0">04-5550172</div><div class="bar" style="margin-top:16px"></div>
</div>
<div class="fcol" style="left:739px">
  <svg width="22" height="22" viewBox="0 0 22 22"><circle cx="11" cy="11" r="10" fill="none" stroke="#f6c225" stroke-width="1.5"/><rect x="6" y="7.5" width="10" height="7" fill="none" stroke="#fff" stroke-width="1.2"/><path d="M6 8l5 4 5-4" fill="none" stroke="#fff" stroke-width="1.2"/></svg>
  <div class="lbl">email</div><div class="val">selamkaveh@example.org</div><div class="bar"></div>
</div>
<div class="fnav">
  <span style="left:177px">HOME</span>
  <span style="left:265px">ABOUT ▾</span>
  <span style="left:358px">THE COMMUNITY</span>
  <span style="left:503px">PROGRAMS ▾</span>
  <span style="left:622px">NEWS ▾</span>
  <span style="left:710px">ADVOCACY</span>
  <span style="left:830px">PARTNERS</span>
  <span style="left:955px">SUPPORT US</span>
</div>
<div class="abs copy" style="left:0;top:3966px;width:1200px;text-align:center;font-size:10px">Copyright © 2022 Selam Kaveh. All Rights Reserved</div>

</body>
</html>
```